I work in creative/artistic projects across different mediums.
It needs to communicate creativity, style, sexy, uniqueness, individuality and sophistication.
It should not look corporate.
Colours I like are black silver gold deep purple, chocolate, orchid.
It doesn't have to make use of all these colours.
I do not like bright primary colors.
Updates

Project Deadline Extended
Reason: Still in the communication process and to allow the person enough time to finish the design. Though i should know in the next day or two. Thank you.

Target Market(s)

creatives and companies wanting to inject creativity into thier business.

Industry/Entity Type

Work

Contact Information for Business Card

Marcus Tellwick
0418592036
marcus@marcustellwick.com

quietgoldenhour.com.au

Requirements
Should not have
• Anything corporate OR OLD FASHIONED

```html
<!DOCTYPE html>
<html lang="en">
<head>
<meta charset="utf-8">
<title>Marcus Tellwick — Business Card</title>
<link rel="stylesheet" href="https://fonts.googleapis.com/css2?family=Advent+Pro:wght@200;300&display=swap">
<style>
  :root {
    --card-width: 742px;
    --card-height: 1200px;
    --charcoal: #2c2a2c;
    --deep-purple: #6d037b;
    --glow-purple: #66066f;
    --text-white: #ffffff;
  }

  html, body {
    margin: 0;
    padding: 0;
    width: var(--card-width);
    height: var(--card-height);
    overflow: hidden;
    background: var(--charcoal);
  }

  .card {
    position: relative;
    width: var(--card-width);
    height: var(--card-height);
    font-family: "Advent Pro", "Helvetica Neue", Arial, sans-serif;
    color: var(--text-white);
  }

  .card__mark-panel {
    position: absolute;
    top: 0;
    left: 0;
    width: 100%;
    height: 600px;
    background: radial-gradient(circle at 50% 52%, var(--glow-purple) 0%, #4d1254 38%, #362438 68%, var(--charcoal) 100%);
    display: flex;
    align-items: center;
    justify-content: center;
  }

  .card__wordmark {
    font-weight: 200;
    font-size: 72px;
    letter-spacing: 2px;
    line-height: 1;
    color: var(--text-white);
  }

  .card__info-panel {
    position: absolute;
    top: 600px;
    left: 0;
    width: 100%;
    height: 600px;
    background: var(--deep-purple);
  }

  .card__name {
    position: absolute;
    top: 52px;
    left: 0;
    width: 100%;
    margin: 0;
    text-align: center;
    font-weight: 200;
    font-size: 96px;
    line-height: 1;
    letter-spacing: 1px;
  }

  .card__contact {
    position: absolute;
    top: 300px;
    left: 0;
    width: 100%;
    margin: 0;
    text-align: center;
    font-style: normal;
    font-weight: 200;
    font-size: 56px;
    line-height: 79px;
  }

  .card__contact span {
    display: block;
  }
</style>
</head>
<body>
  <main class="card">
    <section class="card__mark-panel">
      <span class="card__wordmark">tellwick</span>
    </section>
    <section class="card__info-panel">
      <h1 class="card__name">marcus tellwick</h1>
      <address class="card__contact">
        <span class="card__phone">0418592036</span>
        <span class="card__email">marcus@marcustellwick.com</span>
        <span class="card__web">quietgoldenhour.com.au</span>
      </address>
    </section>
  </main>
</body>
</html>
```